Card design for Heating and Cooling company

this is for a heating and cooling company we recently updated our logo and need to update our cards. We attached our logo so you can incorporate it into the card. We specialize in residential and commercial furnace and air condition repairs. Have been in business since 2014.

Phone number 555.284.9137

We need the following phrases
:Repairs, Installations, and maintenance
:Quality work at reasonable prices
:residential/commercial
:Licensed &Insured
:Email Pinegrovehvac47@mailbox-example.com
Name: Teodor K (Ted)
Also on back side I would like my logo with wording :Thank you for your business and refferal

Industry/Entity Type

Hvac

Contact Information for Business Card

:residential/commercial
:Licensed & Insured
Name: Teodor K (Ted)
Number:555.284.9136

Requirements
Must have
• Blue and red colors
Nice to have
• Maybe a pic of a furnace or air conditioner

```html
<!DOCTYPE html>
<html lang="en">
<head>
<meta charset="utf-8">
<title>Pinegrove Business Card</title>
<link rel="stylesheet" href="https://fonts.googleapis.com/css2?family=Questrial&family=Arimo:wght@400;700&display=swap">
<style>
  :root {
    --red: #ff1500;
    --blue: #15b2de;
    --ink: #111111;
    --white: #ffffff;
    --page: #ffffff;
  }
  * { margin: 0; padding: 0; box-sizing: border-box; }
  html, body { width: 1200px; height: 1000px; overflow: hidden; background: var(--page); }
  .canvas { position: relative; width: 1200px; height: 1000px; }

  .card {
    position: absolute;
    left: 309px;
    width: 568px;
    height: 325px;
    background: var(--white);
    overflow: hidden;
    box-shadow: 6px 10px 14px rgba(0,0,0,0.35);
    font-family: "Arimo", Arial, sans-serif;
  }
  .card--front { top: 161px; }
  .card--back { top: 569px; overflow: visible; }

  .front-panel { position: absolute; inset: 0; }

  .band { position: absolute; left: 0; width: 100%; height: 27px; background: var(--blue); }
  .band--bottom { bottom: 0; }
  .band--top { top: 0; }

  .brand {
    position: absolute;
    display: flex;
    align-items: center;
    gap: 7px;
    font-family: "Arimo", Arial, sans-serif;
    font-weight: 700;
    font-size: 20px;
    letter-spacing: 0.5px;
    color: var(--ink);
  }
  .brand__dot { width: 14px; height: 14px; border-radius: 50%; background: var(--blue); }
  .card--front .brand { left: 48px; top: 87px; }
  .card--back .brand { left: 50%; top: 145px; transform: translateX(-50%); }

  .holder {
    position: absolute;
    right: 22px;
    top: 20px;
    font-family: "Questrial", Arial, sans-serif;
    font-weight: 700;
    font-size: 26px;
    color: var(--ink);
    -webkit-text-stroke: 0.6px var(--ink);
    white-space: nowrap;
  }
  .contact { position: absolute; right: 22px; top: 67px; list-style: none; }
  .contact li {
    display: flex; align-items: center; justify-content: flex-end; gap: 8px;
    color: var(--white); font-size: 15px; height: 27px; white-space: nowrap;
  }
  .contact li.contact__email { font-size: 13px; }
  .contact svg { width: 16px; height: 16px; flex: none; }

  .services {
    position: absolute; left: 20px; top: 197px; list-style: none;
    font-size: 15.5px; line-height: 19px; color: var(--ink); white-space: nowrap;
  }

  .tab { position: absolute; top: 121px; width: 18px; height: 79px; background: var(--red); }
  .tab--left { left: 18px; border-radius: 0 6px 6px 0; }
  .tab--right { right: 18px; border-radius: 6px 0 0 6px; }

  .thanks {
    position: absolute; left: 0; width: 100%; top: 244px;
    text-align: center; font-size: 17.7px; color: var(--ink);
  }
</style>
</head>
<body>
<div class="canvas">

  <section class="card card--front" aria-label="Card front">
    <svg class="front-panel" viewBox="0 0 568 325" preserveAspectRatio="none" aria-hidden="true">
      <polygon points="242,0 568,0 568,298 352,298" fill="var(--red)"/>
    </svg>
    <div class="brand"><span class="brand__dot"></span>PINEGROVE</div>

    <h1 class="holder">Teodor K (Ted)</h1>
    <ul class="contact">
      <li>555.284.9136
        <svg viewBox="0 0 16 16" aria-hidden="true"><path d="M4 2l2.5 3-1.5 1.5c.8 1.8 2.2 3.2 4 4L10.5 9 13.5 11.5 12 14C7 14 2 9 2 4z" fill="var(--blue)"/></svg>
      </li>
      <li class="contact__email">Pinegrovehvac47@mailbox-example.com
        <svg viewBox="0 0 16 16" aria-hidden="true"><rect x="1" y="3" width="14" height="10" fill="var(--blue)"/><path d="M1 3l7 6 7-6" fill="none" stroke="var(--white)" stroke-width="1.2"/></svg>
      </li>
    </ul>

    <ul class="services">
      <li>-Repairs, Installations, and maintenance</li>
      <li>-Quality work at reasonable prices</li>
      <li>-residential/commercial</li>
      <li>-Licensed &amp; Insured</li>
    </ul>

    <div class="band band--bottom"></div>
  </section>

  <section class="card card--back" aria-label="Card back">
    <div class="band band--top"></div>
    <div class="tab tab--left"></div>
    <div class="tab tab--right"></div>
    <div class="brand"><span class="brand__dot"></span>PINEGROVE</div>
    <p class="thanks">Thank you for your business and refferal</p>
    <div class="band band--bottom"></div>
  </section>

</div>
</body>
</html>
```